Corvid Lens Studio Business Card Design

I need a business card designed for a photography business based in Perth, Western Australia called Corvid Lens Studio.

We specialise in wedding, event photography and portrait photography.

The business card must borrow the style of the attached logo.

The hex codes for the colours in the logo are:
#ED1D85 - Pink
#89C23E - Green
#37282F - Black

The name on the card will be:
Name: Tobiah
Phone: 0417395268
Website: www.corvidlensstudio.com.au
Facebook: corvidlensstudio

I am open and happy to accept creative concepts.

Industry/Entity Type

Business

```html
<!DOCTYPE html>
<html lang="en">
<head>
<meta charset="utf-8">
<title>Corvid Lens Studio – Business Card</title>
<link href="https://fonts.googleapis.com/css2?family=Lato:wght@300;400;700&display=swap" rel="stylesheet">
<style>
  :root {
    --backdrop: #e4e4e6;
    --card: #ffffff;
    --band: #050505;
    --ink: #1a1a1a;
    --muted: #5f5f5f;
    --brand-text: #4a4a4a;
    --pink: #ED1D85;
    --shadow: rgba(0, 0, 0, 0.18);
  }
  * { box-sizing: border-box; margin: 0; padding: 0; }
  html, body {
    width: 1200px;
    height: 926px;
    overflow: hidden;
    background: var(--backdrop);
    font-family: "Lato", sans-serif;
  }
  .sheet {
    width: 1200px;
    height: 926px;
    display: flex;
    flex-direction: column;
    align-items: center;
    justify-content: center;
    gap: 42px;
  }
  .card {
    position: relative;
    width: 700px;
    height: 400px;
    background: var(--card);
    box-shadow: 0 6px 18px var(--shadow);
    overflow: hidden;
  }

  /* Front */
  .front-band {
    position: absolute;
    left: 0;
    top: 100px;
    width: 540px;
    height: 210px;
    background: var(--band);
    border-radius: 0 8px 8px 0;
    display: flex;
    flex-direction: column;
    align-items: center;
    justify-content: center;
    gap: 22px;
  }
  .brand-dot {
    width: 56px;
    height: 56px;
    border-radius: 50%;
    background: var(--pink);
  }
  .brand-name {
    font-weight: 300;
    font-size: 17px;
    letter-spacing: 0.62em;
    color: var(--brand-text);
    text-transform: uppercase;
    padding-left: 0.62em;
  }
  .holder-name {
    position: absolute;
    right: 38px;
    top: 50%;
    transform: translate(50%, -50%) rotate(-90deg);
    transform-origin: center;
    font-weight: 400;
    font-size: 38px;
    letter-spacing: 0.04em;
    color: var(--ink);
    text-transform: uppercase;
    white-space: nowrap;
  }

  /* Back */
  .back-band {
    position: absolute;
    left: 150px;
    top: 95px;
    right: 0;
    height: 175px;
    background: var(--band);
    border-radius: 8px 0 0 8px;
    padding: 38px 0 0 40px;
  }
  .contact-list {
    list-style: none;
    font-size: 19px;
    line-height: 1.42;
    color: var(--muted);
    letter-spacing: 0.02em;
  }
  .contact-label {
    font-weight: 700;
    text-transform: uppercase;
  }
</style>
</head>
<body>
  <main class="sheet">
    <section class="card card-front" aria-label="Business card front">
      <div class="front-band">
        <span class="brand-dot" aria-hidden="true"></span>
        <span class="brand-name">Corvid Lens Studio</span>
      </div>
      <span class="holder-name">Tobiah</span>
    </section>

    <section class="card card-back" aria-label="Business card back">
      <div class="back-band">
        <ul class="contact-list">
          <li><span class="contact-label">Phone:</span> 0417395268</li>
          <li><span class="contact-label">Facebook:</span> corvidlensstudio</li>
          <li><span class="contact-label">Web:</span> www.corvidlensstudio.com.au</li>
        </ul>
      </div>
    </section>
  </main>
</body>
</html>
```